Course flyer - evolutive design

We want to have a nice design for our course programm.
In fact we are school language, and our course programm change approximatively each 2 weeks§.
For that we need a design that we can modify each 2 weeks (only dates change ) by ourselves.
We used to have a classical design but we want to upgrade it with a modern and attractive design.
We can have 3 versions one for each city.
We have 3 offices: Tunis, Sousse & Sfax
Attached you can find old designs

Target Market(s)

students from 16 years old till retired people 76 years old

Industry/Entity Type

Education

Font styles to use
Sans Serif

Requirements
Must have
• clear timing for courses (date, days, timing)
• prices
• Adresse (each flyer has its own adress)
• phone Number
• Cool image
Should not have
• Racism
• Violence
• Too much stuff

```html
<!DOCTYPE html>
<html lang="fr">
<head>
<meta charset="utf-8">
<title>Cours d'allemand – Sfax – Mai/Juin 2016</title>
<link rel="stylesheet" href="https://fonts.googleapis.com/css2?family=Oswald:wght@400;600;700&family=Roboto+Condensed:wght@400;700&display=swap">
<style>
  :root{
    --navy:#232a4a;
    --title-blue:#3b8fd9;
    --yellow:#f5c518;
    --flag-black:#141414;
    --flag-red:#d2131c;
    --flag-gold:#f4bf16;
    --white:#ffffff;
    --photo-a:#e9b48e;
    --photo-b:#c27a4f;
    --photo-c:#f3dcc6;
  }
  *{margin:0;padding:0;box-sizing:border-box}
  html,body{width:847px;height:1200px;overflow:hidden;background:var(--white)}
  .flyer{position:relative;width:847px;height:1200px;overflow:hidden;background:var(--white);
    font-family:"Roboto Condensed",Arial,sans-serif;color:var(--white)}

  .flag-waves{position:absolute;left:0;top:0;width:847px;height:200px}

  .brand-name{position:absolute;left:30px;top:38px;font-weight:700;font-size:40px;
    color:var(--flag-gold);line-height:1;font-family:"Roboto Condensed",Arial,sans-serif}

  .period{position:absolute;right:28px;top:30px;text-align:right;font-family:"Oswald",Arial,sans-serif;line-height:1}
  .period-months{font-size:30px;font-weight:600;letter-spacing:1px}
  .period-months span{font-weight:400}
  .period-year{font-size:50px;font-weight:400;margin-top:2px}

  .schedule-band{position:absolute;left:0;top:215px;width:847px;height:630px;background:var(--navy)}

  .title{position:absolute;right:25px;top:292px;font-family:"Oswald",Arial,sans-serif;font-weight:700;
    color:var(--title-blue);font-size:72px;line-height:0.95;text-align:right;letter-spacing:-0.5px}

  .student-photo{position:absolute;left:355px;top:455px;width:205px;height:375px;
    background:linear-gradient(180deg,#e6c27a 0%,#f0a43a 40%,#5b88b8 70%,#34597e 100%);
    border-radius:100px 100px 24px 24px}

  .course{position:absolute;font-family:"Oswald",Arial,sans-serif}
  .course h2{color:var(--yellow);font-size:22px;font-weight:600;line-height:1.05;letter-spacing:.5px}
  .course .rhythm{color:var(--yellow);font-family:"Roboto Condensed",Arial,sans-serif;font-size:15px;font-weight:700;margin-bottom:6px}
  .course .dates{color:var(--yellow);font-size:21px;font-weight:600;margin:8px 0 4px}
  .course ul{list-style:none;font-size:17px;line-height:1.42;letter-spacing:.3px}
  .course ul b{font-weight:600;margin-right:6px}
  .intensif{left:34px;top:385px}
  .extensif-3{left:190px;top:385px}
  .extensif-2{left:190px;top:560px}

  .notes{position:absolute;left:585px;top:452px;width:240px;list-style:none;font-size:15px;line-height:1.3}
  .notes li{padding-left:14px;position:relative;margin-bottom:7px}
  .notes li::before{content:"";position:absolute;left:0;top:7px;width:6px;height:6px;border-radius:50%;background:var(--white)}
  .price{position:absolute;left:599px;top:620px;color:var(--yellow);font-weight:700;font-size:15px}

  .office{position:absolute;left:585px;top:648px;width:250px;font-style:normal}
  .office-city{font-family:"Oswald",Arial,sans-serif;font-weight:700;font-size:56px;line-height:1;letter-spacing:1px}
  .office-address{font-size:13px;line-height:1.3;margin-top:6px}
  .office-contact{font-size:13px;line-height:1.3;margin-top:6px}
  .social{display:flex;align-items:center;gap:8px;font-size:13px;margin-top:8px}
  .social-square{width:14px;height:14px;background:var(--white)}

  .group-photo{position:absolute;left:0;top:845px;width:847px;height:355px;
    background:linear-gradient(100deg,var(--photo-c) 0%,var(--photo-a) 35%,var(--photo-b) 65%,#6d4a38 100%)}
</style>
</head>
<body>
<main class="flyer">

  <svg class="flag-waves" viewBox="0 0 847 200" aria-hidden="true">
    <path d="M260 0 H847 V40 C700 70 520 30 260 0Z" fill="var(--flag-black)"/>
    <path d="M230 0 C480 40 680 80 847 40 V120 C660 150 470 80 230 0Z" fill="var(--flag-red)"/>
    <path d="M230 0 C470 80 660 150 847 120 V175 C640 200 440 110 230 0Z" fill="var(--flag-gold)"/>
  </svg>

  <div class="brand-name">Lingora</div>

  <div class="period">
    <div class="period-months">MAI <span>JUIN</span></div>
    <div class="period-year">2016</div>
  </div>

  <section class="schedule-band"></section>

  <h1 class="title">COURS<br>D'ALLEMAND</h1>

  <div class="student-photo" role="img" aria-label="Jeune étudiante souriante tenant des cahiers"></div>

  <div class="course intensif">
    <h2>INTENSIF</h2>
    <p class="rhythm">(Lundi - Vendredi)</p>
    <p class="dates">07/03 - 25/03</p>
    <ul>
      <li><b>A1.1</b>DKS2090</li>
      <li><b>A1.2</b>DKS2091</li>
      <li><b>A2.1</b>DKS2092</li>
      <li><b>A2.2</b>DKS2093</li>
      <li><b>B1.1</b>DKS2098</li>
      <li><b>B1.2</b>DKS2099</li>
      <li><b>B2.1</b>DKS2094</li>
    </ul>
    <p class="dates">28/03 - 15/04</p>
    <ul>
      <li><b>A1.1</b>DKS2105</li>
      <li><b>A1.2</b>DKS2106</li>
      <li><b>A2.1</b>DKS2107</li>
      <li><b>A2.2</b>DKS2108</li>
    </ul>
  </div>

  <div class="course extensif-3">
    <h2>EXTENSIF</h2>
    <p class="rhythm">(3 jours / semaine)</p>
    <ul>
      <li><b>A1.1</b>DKS2121</li>
      <li><b>A1.2</b>DKS2122</li>
      <li><b>A2.2</b>DKS2124</li>
    </ul>
  </div>

  <div class="course extensif-2">
    <h2>EXTENSIF</h2>
    <p class="rhythm">(2 jours / semaine)</p>
    <p class="dates">28/03 - 22/04</p>
    <ul>
      <li><b>A1.1</b>DKS2115</li>
      <li><b>A1.2</b>DKS2116</li>
      <li><b>A2.1</b>DKS2117</li>
      <li><b>A2.2</b>DKS2118</li>
      <li><b>B1.1</b>DKS2119</li>
      <li><b>B1.2</b>DKS2120</li>
    </ul>
  </div>

  <ul class="notes">
    <li>Toute inscription doit impérativement se faire au plus tard une semaine avant le début des cours.</li>
    <li>Nombre minimum de 4 participants requis.</li>
    <li>L'horaire des cours est susceptible d'être modifié.</li>
  </ul>
  <p class="price">Prix par module 240 TND.</p>

  <address class="office">
    <div class="office-city">SFAX</div>
    <p class="office-address">Avenue des Oliviers,<br>Rue Hédi Karray,<br>Immeuble Nour (2ème étage)</p>
    <p class="office-contact">Tel.: +216 74 000 123<br>Email: contact-sfax@lingora.org<br>Web: www.lingora.org</p>
    <p class="social"><span class="social-square"></span>www.social.example/lingora</p>
  </address>

  <div class="group-photo" role="img" aria-label="Groupe d'étudiants souriants côte à côte"></div>

</main>
</body>
</html>
```